Website Design Project

KEL VISA is looking for a professional designer who would re-design our current website www.bordwellpassage.com.
KEL provides immigration and visa services to the US in these markets: Slovakia, Czech republic and USA. We would like to target Poland and Russia as well.
Who are we: KEL is Dubrik & Helmsley international law firm with offices in New York, Bratislava and Prague. We are licensed in several jurisdiction such as New York, England and Wales, and Slovakia.
Additionally, we are offering online products in our E-shop, such as E-books, E-brochures, DVD's regarding visa and immigration opportunities into United States.
Our targeted audience is: young students who want to study in the US, young professionals looking for employment in the US, investors who want to invest to the US, people looking to get their green card (permanent residency in the US), etc.
Our new design: should look professional, communicate financial safety, professional services, increase sales, but also feel emotional for people who are looking forward to start their new life in the United States.
Updates

Dear Designers, 

we have changed our project from refundable to committed! 

Cant wait to see your designs! 

Thanks! 

KEL VISA 

Designers! 

We have attached pictures od old NY so you may wanna work with them! 

Target Market(s)

USA, Slovakia, Czech Republic

Industry/Entity Type

Financial

Requirements
Nice to have
• 1) pictures of old New York, Tarrow Quay.
2) pictures of the US
Should not have
• KEL VISA is operated by law form Dubrik & Helmsley. We are not looking for boring, old fashioned and profesional website for "legal practitioners". No dark colors, no brown color, no dark green color. it should look light and fresh.

KEL VISA is fresh, new, modern, professional and flexible TEAM of YOUNG and SMART immigration lawyers who want to make a difference. Our website MUST reflect our philosophy. "Success is all about people that we meet and the things we create with them".

```html
<!DOCTYPE html>
<html lang="en">
<head>
<meta charset="utf-8">
<title>KEL VISA – Visa and Immigration</title>
<link rel="stylesheet" href="https://fonts.googleapis.com/css2?family=Open+Sans:wght@400;600&family=Arimo:ital,wght@0,400;0,700;1,400&display=swap">
<style>
:root{
  --blue:#64acd8;
  --blue-dark:#4f97c6;
  --orange:#f39a2b;
  --text:#2f2f2f;
  --muted:#555;
  --rule:#d9d9d9;
  --panel:#f3f3f3;
  --white:#fff;
}
*{margin:0;padding:0;box-sizing:border-box}
html,body{width:1059px;height:1200px;overflow:hidden;background:var(--white)}
body{position:relative;font-family:"Arimo",Arial,sans-serif;color:var(--text);font-size:11px;letter-spacing:.4px}
.abs{position:absolute}
.brand{left:97px;top:8px;font-family:"Open Sans",sans-serif;font-weight:600;font-size:32px;color:var(--blue);letter-spacing:0}
.tagline{left:97px;top:45px;font-style:italic;font-size:10.5px;color:#333;letter-spacing:0}
.callus{right:97px;top:13px;font-family:"Open Sans",sans-serif;font-size:13px;color:#555;letter-spacing:0}
.callus b{color:var(--orange);font-weight:400;margin-left:4px}
.search{left:771px;top:34px;width:191px;height:21px;border:1px solid #bbb;border-radius:11px;font-style:italic;font-size:9.5px;color:#777;padding:4px 13px;letter-spacing:0}
.search svg{position:absolute;right:9px;top:5px}
.nav{left:0;top:69px;width:1059px;height:38px;background:var(--blue);display:flex;padding-left:97px}
.nav a{font-family:"Open Sans",sans-serif;font-size:11.5px;color:var(--white);text-decoration:none;line-height:38px;padding:0 14px;border-left:1px solid rgba(255,255,255,.45);letter-spacing:0}
.nav a:first-child{padding-left:0;border-left:0}
.hero{left:0;top:107px;width:1059px;height:299px;background:linear-gradient(180deg,#e9e9e9 0%,#9a9a9a 45%,#6e6e6e 80%,#a5a5a5 100%)}
.quote{left:97px;top:302px;font-family:"Open Sans",sans-serif;font-size:30px;line-height:32px;color:var(--white);letter-spacing:0}
.hero-more{left:632px;top:360px;font-family:"Open Sans",sans-serif;font-style:italic;font-size:13px;color:var(--white)}
.dots{left:907px;top:389px;display:flex;gap:7px}
.dots i{width:9px;height:9px;border-radius:50%;background:#444;display:block}
.dots i:first-child{background:var(--blue)}
.welcome{left:97px;top:432px;width:865px;border-bottom:1px solid var(--rule);padding-bottom:6px;font-family:"Open Sans",sans-serif;font-weight:600;font-size:19px;color:var(--blue);letter-spacing:.3px}
.photo{background:linear-gradient(150deg,#7aa9d6,#2f63a8 60%,#1e4f95)}
.intro-img{left:97px;top:477px;width:143px;height:96px}
.intro-title{left:266px;top:476px;font-family:"Open Sans",sans-serif;font-size:17px;color:#333;letter-spacing:0}
.intro-text{left:266px;top:501px;width:696px;line-height:16px;text-align:justify;font-size:10.5px}
.btn{left:882px;top:549px;width:80px;height:23px;background:var(--blue);color:var(--white);border-radius:2px;font-size:10.5px;line-height:23px;text-align:center}
.panel{background:var(--panel)}
.panel h3{font-family:"Open Sans",sans-serif;font-weight:400;font-size:16px;color:var(--blue);padding:14px 8px 4px;border-bottom:1px solid var(--rule);letter-spacing:0}
.links{left:97px;top:613px;width:214px;height:178px}
.links li{list-style:none;display:flex;justify-content:space-between;margin:0 8px;padding:10px 0 4px;border-bottom:1px dotted #999;font-size:10.5px}
.links li:last-child{border-bottom:0}
.links li span{font-size:9.5px}
.products{left:97px;top:808px;width:214px;height:187px}
.prod{display:flex;gap:9px;margin:0 8px;padding:14px 0 10px;border-bottom:1px dotted #999}
.prod:last-child{border-bottom:0}
.prod .thumb{width:66px;height:48px;flex:none;border:1px solid #ccc}
.prod b{display:block;font-family:"Open Sans",sans-serif;font-weight:400;font-size:13.5px;color:#333;letter-spacing:0}
.prod p{font-size:10.5px;line-height:13px;color:var(--muted);letter-spacing:.8px}
.services{left:363px;top:622px;width:334px}
.svc{display:flex;gap:26px;height:97px;border-bottom:1px dotted #999;padding-top:0}
.svc:last-child{border-bottom:0}
.svc .thumb{width:61px;height:58px;flex:none}
.svc h4{font-family:"Open Sans",sans-serif;font-weight:400;font-size:16px;color:var(--blue);letter-spacing:.3px;margin-top:2px}
.svc p{font-size:10px;line-height:16px;margin-top:4px}
.svc em{font-style:normal;color:var(--orange)}
.posts{left:748px;top:612px;width:214px;height:383px}
.post{margin:0 9px;padding:12px 0 8px;border-bottom:1px dotted #999}
.post:last-child{border-bottom:0}
.post small{display:block;font-style:italic;font-size:9.5px;letter-spacing:0}
.post p{font-size:10.5px;line-height:12px;text-align:justify;letter-spacing:.8px}
.post a{display:block;text-align:right;font-style:italic;color:var(--orange);text-decoration:none;font-size:10.5px;margin-top:10px;letter-spacing:0}
.footer{left:0;top:1035px;width:1059px;height:165px;background:var(--blue);color:var(--white)}
.fcol{position:absolute;top:20px}
.fcol h5{font-size:12px;font-weight:700;padding-bottom:6px;border-bottom:1px dotted rgba(255,255,255,.7);margin-bottom:6px;letter-spacing:.5px}
.fcol p,.fcol li{font-size:9.5px;line-height:16px;letter-spacing:1px;list-style:none}
.social{display:flex;gap:12px;margin-top:4px}
.social i{width:14px;height:14px;border-radius:50%;background:var(--white);display:block}
.testimonial{font-style:italic;font-size:10.5px;line-height:16px;text-align:justify;padding-left:17px;position:relative}
.testimonial svg{position:absolute;left:0;top:1px}
.author{text-align:right;font-style:italic;font-size:10.5px;margin-top:12px}
.copy{left:0;width:1059px;top:1178px;text-align:center;color:var(--white);font-size:10.5px;letter-spacing:1px}
</style>
</head>
<body>
<header>
  <div class="abs brand">KEL VISA</div>
  <div class="abs tagline">Dubrik &amp; Helmsley Immigration Attorneys, US Visa, US Green Card, ESTA</div>
  <div class="abs callus">Call us today on <b>(212) 555-0147</b></div>
  <div class="abs search">Search something...
    <svg width="10" height="10" viewBox="0 0 10 10"><circle cx="4" cy="4" r="3" fill="none" stroke="#999" stroke-width="1.3"/><line x1="6.3" y1="6.3" x2="9.3" y2="9.3" stroke="#999" stroke-width="1.5"/></svg>
  </div>
</header>
<nav class="abs nav">
  <a>Consultation</a><a>Visitors Visas</a><a>Work Visas</a><a>Business Visas</a><a>Family Visas</a><a>Student Visas</a><a>Green Card</a><a>Visa Forms</a><a>KEL E-shop</a><a>Visa News</a>
</nav>
<section class="abs hero" role="img" aria-label="Black and white photo of a suspension bridge in front of the New York skyline at dusk"></section>
<div class="abs quote">"Success is all about people that we meet and<br>the things we create with them"</div>
<div class="abs hero-more">Read more</div>
<div class="abs dots"><i></i><i></i><i></i><i></i></div>

<h2 class="abs welcome">WELCOME TO KEL VISA AND IMMIGRATION</h2>
<div class="abs intro-img photo" role="img" aria-label="Photo of the Statue of Liberty against a blue sky"></div>
<h3 class="abs intro-title">Visas to the U.S. and U.S. Immigration</h3>
<p class="abs intro-text">Lorem Ipsum is simply dummy text of the printing and typesetting industry. Lorem Ipsum has been the industry's standard dummy text ever since the 1500s, when an unknown printer took a galley of type and scrambled it to make a type specimen book. It has survived not only five centuries, but also the leap into electronic typesetting, remaining</p>
<div class="abs btn">› Read more</div>

<aside class="abs panel links">
  <h3>Important Links</h3>
  <ul>
    <li>Visa Forms Download<span>Free</span></li>
    <li>Business Visa for 6 Months<span>$400</span></li>
    <li>Tourist Visa for 6 Months<span>$300</span></li>
    <li>ESTA Registration<span>$50</span></li>
    <li>Consultation<span>$65</span></li>
  </ul>
</aside>
<aside class="abs panel products">
  <h3>KEL E-Products</h3>
  <div class="prod"><div class="thumb" role="img" aria-label="Photo of stacked colourful DVD discs" style="background:linear-gradient(120deg,#d8e6f5,#b59fe0,#e5a7d8)"></div><div><b>Visa DVD</b><p>Lorem ipsum dolor jit amet,consectetuer</p></div></div>
  <div class="prod"><div class="thumb" role="img" aria-label="Scan of a printed visa application form" style="background:#f7f7f7"></div><div><b>Visa Forms</b><p>Lorem ipsum dolor sit amet,consectetuer</p></div></div>
</aside>

<section class="abs services">
  <div class="svc"><div class="thumb photo" role="img" aria-label="Photo of a smiling businessman" style="background:linear-gradient(#8fbf7a,#e6e0d8)"></div><div><h4>E-2 Investor Visa</h4><p>Lorem Ipsum is simply dummy text of the printing and type industry...[ <em>more</em> ]</p></div></div>
  <div class="svc"><div class="thumb photo" role="img" aria-label="Photo of a young professional at a laptop" style="background:linear-gradient(#e8e4e0,#b9a89a)"></div><div><h4>H1B Work Visa</h4><p>Lorem Ipsum is simply dummy text of the printing and type industry...[ <em>more</em> ]</p></div></div>
  <div class="svc"><div class="thumb photo" role="img" aria-label="Photo of a bride and groom outdoors" style="background:linear-gradient(#9cc27e,#e9e7e2)"></div><div><h4>Marriage Visa</h4><p>Lorem Ipsum is simply dummy text of the printing and type industry...[ <em>more</em> ]</p></div></div>
  <div class="svc"><div class="thumb photo" role="img" aria-label="Photo of a happy family of four" style="background:linear-gradient(#f1ede6,#c99b7c)"></div><div><h4>Green Card</h4><p>Lorem Ipsum is simply dummy text of the printing and type industry...[ <em>more</em> ]</p></div></div>
</section>

<aside class="abs panel posts">
  <h3>Recent Posts</h3>
  <div class="post"><small>Posted on Dec 1st, 2012</small><p>Lorem Ipsum is simply dummy text the lokknyi nyment printing.</p><a>› Read more</a></div>
  <div class="post"><small>Posted on Nov 7th, 2012</small><p>Lorem Ipsum is simply dummy text the lokknyi nyment printing.</p><a>› Read more</a></div>
  <div class="post"><small>Posted on October 10th, 2012</small><p>Lorem Ipsum is simply dummy text the lokknyi nyment printing.</p><a>› Read more</a></div>
  <div class="post"><small>Posted on October 5th, 2012</small><p>Lorem Ipsum is simply dummy text the lokknyi nyment printing.</p><a>› Read more</a></div>
</aside>

<footer class="abs footer">
  <div class="fcol" style="left:97px;width:157px"><h5>Links</h5>
    <ul><li>▪ Partner Pages</li><li>▪ Dubrik &amp; Helmsley</li><li>▪ Meridian Foundation</li><li>▪ Crestline Holdings LLC Ltd.<br>&nbsp;&nbsp;in USA England Hong Kong or<br>&nbsp;&nbsp;Offshore</li></ul></div>
  <div class="fcol" style="left:315px;width:111px"><h5>Contact Us</h5>
    <p>Dubrik &amp; Helmsley<br>New York<br>48 W 71st Street #4B<br>New York 10023 NY<br>+1 (212) 555-0147</p></div>
  <div class="fcol" style="left:491px;width:108px"><h5>Get Connected</h5>
    <div class="social"><i></i><i></i><i></i></div></div>
  <div class="fcol" style="left:667px;width:295px"><h5>Testimonial</h5>
    <p class="testimonial"><svg width="12" height="10" viewBox="0 0 12 10"><path d="M1 10V6Q1 2 5 1V3Q3 4 3 6H5V10ZM7 10V6Q7 2 11 1V3Q9 4 9 6H11V10Z" fill="#fff"/></svg>Praesent uluoles tie lacus. Aenean non ummyen drerit maurisus porta. Fuse suscip iquam erat volut patis ais. Integer lacibul libro nisl porta.</p>
    <p class="author">- Mr. Jonas Verel</p></div>
</footer>
<div class="abs copy">© 2012 KEL Visa and Immigration. All Rights Reserved</div>
</body>
</html>
```